Velmora Care Collective Presentation Folder, for Cancer Awareness, VERY COLORFUL AND MODERN

Presentation Folder I know pretty much what i want so it should be very eazy , I have included files from folders I use now rebrand them to my new company they will be fine, no sense re creating the wheel
Full Bleed Size
20.87" x 16.68"
53 x 42.4 cm
6260 x 5004 pixels
Document Trim Size
20.75" x 16.56"
52.7 x 42.1 cm
6225 x 4969 pixels

Industry/Entity Type

Medical

Font styles to use
Serif

Colors

Designer to choose colors to be used in the design.

Requirements
Must have
• really I am not looking for some one to redesign, we like our folder front page and would like to see new word information added., there are two folder front pages to choose from
• So Keep the original front page and redesign the back page and the pockets
• Can Make your Design off of one of the ones I already uploaded
Nice to have
• Keep the same color schemes, Keep the original front page and redesign the back page and the pockets
Should not have
• DO not recreate the front covers, use what I gave you and just rebrand

```html
<!DOCTYPE html>
<html lang="en">
<head>
<meta charset="utf-8">
<title>Velmora Care Collective – Presentation Folder</title>
<link rel="stylesheet" href="https://fonts.googleapis.com/css2?family=Raleway:wght@300;400;500;600;700&family=Arimo:wght@400;700&display=swap">
<style>
:root{
  --backdrop-light:#d1d2d4;
  --backdrop-dark:#2b2b2d;
  --paper:#ffffff;
  --dieline:#e2454f;
  --foldline:#8fd19e;
  --brand-red:#e8322f;
  --pink:#f2919b;
  --pink-text:#f08d9a;
  --slate:#8a8c8f;
  --slate-dark:#6d6e70;
  --row-alt:#e6e7e8;
  --ink:#4a4a4c;
  --navy:#1f2a5c;
  --lynch:#f9c232;
  --peutz:#b8cf47;
  --li:#3fae5a;
  --li-soft:#8fd19e;
  --cowden:#2aa0d8;
  --gastric:#6d6e70;
  --gastric-soft:#a7a9ac;
}
*{margin:0;padding:0;box-sizing:border-box}
html,body{width:1200px;height:540px;overflow:hidden}
body{font-family:"Raleway",sans-serif;color:var(--ink)}
.canvas{position:relative;width:1200px;height:540px;overflow:hidden;
  background:linear-gradient(to bottom,var(--backdrop-light) 0 65.3%,var(--backdrop-dark) 65.3% 100%)}
.stage{position:absolute;left:0;top:0;width:1500px;height:675px;transform:scale(.8);transform-origin:0 0}
.abs{position:absolute}
.sheet{position:absolute;background:var(--paper);box-shadow:3px 4px 6px rgba(0,0,0,.35)}
.sheet--outside{left:40px;top:45px;width:725px;height:583px}
.sheet--inside{left:792px;top:47px;width:670px;height:421px}
.fold{position:absolute;border-left:1px dashed var(--foldline)}
.dieline{position:absolute;left:0;top:0;overflow:visible}

/* test menu panel */
.menu{left:56px;top:25px;width:280px}
.menu__lab{font-size:11px;font-weight:500;color:var(--brand-red)}
.menu__title{position:absolute;right:2px;top:2px;font-size:11.5px;font-style:italic;font-weight:700;color:var(--brand-red)}
.menu__title sup{font-size:5px}
.menu__contact{display:flex;justify-content:space-between;font-size:3.6px;color:var(--slate);margin-top:3px;letter-spacing:.2px}
.gene-table{margin-top:10px;font-family:"Arimo",sans-serif;font-size:4.4px;width:280px}
.gene-table .row{display:grid;grid-template-columns:118px 1fr;height:8.75px;align-items:center;padding-left:4px}
.gene-table .row:nth-child(even){background:var(--row-alt)}
.gene-table .gene{color:var(--brand-red);font-weight:700}
.gene-table .organ{color:#333}
.gene-table .head{background:var(--brand-red)!important;color:#fff;font-family:"Raleway",sans-serif;font-weight:600;font-size:5px}
.gene-table .head .gene{color:#fff}
.gene-table .band{color:#fff;font-family:"Raleway",sans-serif;font-weight:600;font-size:5px;display:block;line-height:8.75px}
.band--lynch{background:var(--lynch)!important}
.band--peutz{background:var(--peutz)!important}
.band--li{background:var(--li)!important}
.band--cowden{background:var(--cowden)!important}
.band--gastric{background:var(--gastric)!important}
.tint-lynch{background:var(--lynch)!important}
.tint-li{background:var(--li-soft)!important}
.tint-gastric{background:var(--gastric-soft)!important}

/* front cover */
.cover-title{left:362px;top:41px;width:334px;height:26px;background:var(--pink);color:#fff;
  font-size:12.5px;letter-spacing:1.6px;text-align:center;line-height:26px;font-weight:400}
.cover-tag{left:423px;top:68px;width:204px;height:17px;background:var(--slate);color:#fff;
  font-size:8px;text-align:center;line-height:17px;letter-spacing:.2px}
.cover-ribbon{left:638px;top:67px}
.cover-lede{left:362px;top:96px;width:334px;text-align:center;font-size:7px;line-height:8px;color:#555}
.cover-photo{left:362px;top:113px;width:334px;height:242px;
  background:radial-gradient(ellipse at 55% 45%,#e6e6e6 0%,#b9b9b9 45%,#7d7d7d 100%)}
.cover-strap{left:362px;top:357px;width:334px;height:22px;background:var(--slate);color:#fff;
  font-size:8px;letter-spacing:.8px;text-align:center;line-height:22px}
.cover-brand{left:408px;top:375px;display:flex;align-items:center;gap:4px;font-size:5px;font-weight:600;color:var(--navy)}
.mark{border-radius:50%;background:var(--navy);display:inline-block;flex:none}

/* pockets */
.pocket-strip{background:#d1d3d4}
.pocket-text{transform:rotate(180deg);text-align:center;color:var(--navy);font-weight:700}
.pocket-text--left{left:100px;top:436px;width:184px}
.pocket-text--right{left:430px;top:462px;width:200px;display:flex;flex-direction:column;align-items:center;gap:6px}
.pocket-name{display:block;font-size:12px}
.pocket-sub{display:block;font-size:7px}
.pocket-logo{display:flex;align-items:center;gap:8px}
.pocket-name--large{font-size:17px;line-height:19px;text-align:left}

/* inside */
.inside-copy{left:388px;top:48px;width:256px;font-size:7.6px;line-height:9.8px;text-align:justify;color:#555}
.inside-copy p+p{margin-top:9.5px}
.inside-callout{left:370px;top:214px;width:268px;text-align:center;font-size:14px;line-height:16.5px;color:var(--pink-text);font-weight:400}
</style>
</head>
<body>
<div class="canvas">
 <div class="stage">

  <section class="sheet sheet--outside">
   <svg class="dieline" width="725" height="583" viewBox="0 0 725 583" fill="none" stroke="var(--dieline)" stroke-width="1">
    <path d="M28 3V423H0M0 270a10 10 0 0 1 0 20M697 3V423H725M725 270a10 10 0 0 0 0 20"/>
    <path d="M28 423V560q0 20 20 20H352q6 0 6-8V440L360 423L362 440V572q0 8 6 8H677q20 0 20-20V423"/>
    <path d="M0 3H725"/>
    <path d="M130 465l18 18M240 467l18-18M132 537l16-16M240 521l18 18"/>
   </svg>
   <div class="fold" style="left:28px;top:3px;height:420px"></div>
   <div class="fold" style="left:360px;top:3px;height:420px"></div>
   <div class="fold" style="left:695px;top:3px;height:420px"></div>

   <div class="abs menu">
    <div class="menu__lab">Corbeth Diagnostics</div>
    <div class="menu__title">FORESEE<sup>™</sup> Test Menu</div>
    <div class="menu__contact">
     <span>1450 Harrow Ridge Dr NW · Suite 8 · Marlow, GA 30318<br>(404) 555-0142 · Fax (404) 555-0143 · info@corbethdx.com</span>
     <span>CLIA 00D0000000 · CORBETHDX.COM</span>
    </div>
    <div class="gene-table">
     <div class="row head"><span class="gene">GENE</span><span>CANCER-ASSOCIATED ORGAN/SYSTEMS</span></div>
     <div class="row"><span class="gene">APC</span><span class="organ">Colon</span></div>
     <div class="row"><span class="gene">ATM</span><span class="organ">Breast/Pancreatic/Brain</span></div>
     <div class="row"><span class="gene">BARD1</span><span class="organ">Breast/Ovarian</span></div>
     <div class="row"><span class="gene">BMPR1A</span><span class="organ">Colon</span></div>
     <div class="row"><span class="gene">BRCA1</span><span class="organ">Breast/Ovarian/Prostate</span></div>
     <div class="row"><span class="gene">BRCA2</span><span class="organ">Breast/Ovarian/Prostate</span></div>
     <div class="row"><span class="gene">BRIP1</span><span class="organ">Breast/Ovarian</span></div>
     <div class="row"><span class="gene">CDK4</span><span class="organ">Melanoma</span></div>
     <div class="row"><span class="gene">P16 (CDKN2A)</span><span class="organ">Melanoma/Breast/Pancreatic/Squamous</span></div>
     <div class="row"><span class="gene">FANCC</span><span class="organ">Blood</span></div>
     <div class="row"><span class="gene">MEN1</span><span class="organ">Thyroid/Parathyroid</span></div>
     <div class="row"><span class="gene">MET</span><span class="organ">Renal/Hepatic</span></div>
     <div class="row"><span class="gene">MRE11A</span><span class="organ">Ovarian/Breast</span></div>
     <div class="row"><span class="gene">NBN</span><span class="organ">Breast/Ovarian/Prostate/Melanoma</span></div>
     <div class="row"><span class="gene">NF1</span><span class="organ">Blood</span></div>
     <div class="row"><span class="gene">NTRK1</span><span class="organ">Thyroid/Parathyroid</span></div>
     <div class="row"><span class="gene">PALB2</span><span class="organ">Breast/Ovarian/Pancreatic</span></div>
     <div class="row"><span class="gene">PTCH1</span><span class="organ">Melanoma/Brain/Breast/Colon</span></div>
     <div class="row"><span class="gene">RAD50</span><span class="organ">Breast/Ovarian</span></div>
     <div class="row"><span class="gene">RAD51C</span><span class="organ">Ovarian/Breast</span></div>
     <div class="row"><span class="gene">RAD51D</span><span class="organ">Ovarian/Breast</span></div>
     <div class="row"><span class="gene">RET</span><span class="organ">Lung/Thyroid/Parathyroid</span></div>
     <div class="row"><span class="gene">SMAD4</span><span class="organ">Colon/Pancreas</span></div>
     <div class="row band band--lynch">LYNCH SYNDROME GENES</div>
     <div class="row"><span class="gene">MLH1</span><span class="organ">Colorectal/Ovarian</span></div>
     <div class="row"><span class="gene">MSH2</span><span class="organ">Colorectal/Ovarian</span></div>
     <div class="row"><span class="gene">MSH6</span><span class="organ">Colorectal/Ovarian</span></div>
     <div class="row tint-lynch"><span class="gene">PMS2</span><span class="organ">Colorectal/Ovarian</span></div>
     <div class="row"><span class="gene">EPCAM</span><span class="organ">Colorectal</span></div>
     <div class="row band band--peutz">PEUTZ-JEGHERS SYNDROME GENE</div>
     <div class="row"><span class="gene">STK11</span><span class="organ">Breast/Ovarian/Melanoma/Colorectal/Lung</span></div>
     <div class="row band band--li">LI-FRAUMENI SYNDROME GENE</div>
     <div class="row"><span class="gene">CHEK2</span><span class="organ">Breast/Ovarian/Prostate</span></div>
     <div class="row tint-li"><span class="gene">TP53</span><span class="organ">Breast/Bladder/Ovarian/Squamous</span></div>
     <div class="row band band--cowden">COWDEN SYNDROME GENE</div>
     <div class="row"><span class="gene">PTEN</span><span class="organ">Endometrium/Breast/Prostate/Lung</span></div>
     <div class="row band band--gastric">HEREDITARY DIFFUSE GASTRIC CANCER SYNDROME GENE</div>
     <div class="row"><span class="gene">CDH1</span><span class="organ">Breast/Gastric/Ovarian/Prostate</span></div>
     <div class="row tint-gastric"><span class="gene">VHL</span><span class="organ">Renal</span></div>
    </div>
   </div>

   <h1 class="abs cover-title">HEREDITARY CANCER SCREENING</h1>
   <div class="abs cover-tag">Doctors are the Gatekeepers to Genetic Testing</div>
   <svg class="abs cover-ribbon" width="12" height="20" viewBox="0 0 12 20" aria-label="Awareness ribbon" role="img">
    <path d="M6 2C2 2 2 7 4 10L1 19M6 2c4 0 4 5 2 8l3 9" stroke="var(--pink)" stroke-width="2.4" fill="none"/>
    <path d="M6 2c-4 0-4 5-2 8" stroke="#5b8fd0" stroke-width="2.4" fill="none"/>
   </svg>
   <p class="abs cover-lede">We have an obligation to help patients understand genetic risk<br>and how testing can guide health care decisions.</p>
   <div class="abs cover-photo" role="img" aria-label="Black and white photo of a multi-generation family sharing a meal at an outdoor table"></div>
   <div class="abs cover-strap">The test you order FOR your patients</div>
   <div class="abs cover-brand"><span class="mark" style="width:26px;height:26px"></span>Velmora Care Collective</div>

   <div class="abs pocket-strip" style="left:30px;top:425px;width:22px;height:158px"></div>
   <div class="abs pocket-strip" style="left:672px;top:425px;width:23px;height:158px"></div>

   <div class="abs pocket-text pocket-text--left">
    <span class="pocket-name">Velmora Care Collective</span>
    <span class="pocket-sub">a division of Corvalen Medical Sales LLC</span>
   </div>
   <div class="abs pocket-text pocket-text--right">
    <span class="pocket-logo">
     <span class="mark" style="width:44px;height:44px"></span>
     <span class="pocket-name pocket-name--large">Velmora<br>Care Collective</span>
    </span>
    <span class="pocket-sub">a division of Corvalen Medical Sales LLC</span>
   </div>
  </section>

  <section class="sheet sheet--inside">
   <div class="fold" style="left:334px;top:0;height:421px"></div>
   <div class="abs inside-copy">
    <p>There are many benefits to getting tested, regardless of the eventual result. If one of your family members — however distant — had cancer, there is a chance that you inherited a gene mutation that not only increases your personal risk of cancer, but also could be passed to the next generation. Those who are carriers of hereditary cancer gene mutations, could be at risk of getting cancer earlier in life than the general population. The sooner genetic testing is done, the more likely it is that the risk can be managed appropriately.</p>
    <p>Hereditary cancer screening provides vital information to help people with a strong personal or family history of cancer understand their own risk of developing the disease. With this information, they can take steps to Potentially Prevent Cancer, Delay the Onset of Cancer or Catch it at an Earlier stage when outcomes and survival rates are Better.</p>
   </div>
   <p class="abs inside-callout">Identifying an inherited genetic<br>mutation has the potential<br>to prevent cancer and save lives.</p>
  </section>

 </div>
</div>
</body>
</html>
```